Redesign website for small print company

Vindabrot is a small printing company in Iceland mainly servicing Students, schools, etc. We are also doing all kind of other jobs, like business cards, book printing, brochure printing etc. We are also selling books online.
Our website is: www.vindabrot.is
What we are looking for is:
- Web Design (Uncoded - PSD layout only)
- Mobile friendly design, using our current color scheme: Red, green, yellow and light gray.
- Clean simple design
- Simple, light and easy to use.
- More menu Items/drop down
Industry/Entity Type
Digital Printing
Number of Pages Required
5+ page
Requirements
Must have
- Easy navigation
- Designed for mobile
- Current color scheme (see logo)
Nice to have
- Icon based products

```html
<!DOCTYPE html>
<html lang="en">
<head>
<meta charset="utf-8">
<title>Vindabrot – Print firm in Iceland</title>
<link href="https://fonts.googleapis.com/css2?family=Roboto:wght@400;500;700&family=Open+Sans:wght@400;600;700&display=swap" rel="stylesheet">
<style>
:root{
  --red:#e8312f;
  --green:#2e6b2f;
  --yellow:#f2d52e;
  --dark:#2b2b2b;
  --darker:#1f1f1f;
  --grey:#f3f3f3;
  --text:#333;
  --muted:#666;
  --white:#fff;
}
*{box-sizing:border-box;margin:0;padding:0}
html,body{width:1200px;height:3403px;overflow:hidden}
body{position:relative;font-family:"Open Sans",Arial,sans-serif;color:var(--text);background:var(--white)}
.abs{position:absolute}
.topbar{left:0;top:0;width:1200px;height:38px;background:var(--yellow)}
.topbar .lang{left:154px;top:11px;font-size:13px;font-weight:600}
.topbar .contact{top:8px;display:flex;align-items:center;gap:8px;font-size:13px}
.dot-red{width:26px;height:26px;border-radius:50%;background:var(--red);display:flex;align-items:center;justify-content:center}
.header{left:0;top:38px;width:1200px;height:94px;background:var(--white)}
.brand{display:flex;align-items:center;gap:12px;font-family:"Roboto",sans-serif;font-weight:700;color:var(--dark)}
.brand-mark{width:40px;height:40px;background:var(--yellow)}
.search{left:687px;top:68px;width:238px;height:34px;border:1px solid #ddd;font-size:11px;color:#999;padding:10px 12px}
.search-go{left:925px;top:68px;width:73px;height:34px;background:var(--darker);color:#fff;font-size:13px;text-align:center;line-height:34px}
.nav{left:0;top:132px;width:1200px;height:45px;background:var(--red)}
.nav span{position:absolute;top:0;line-height:45px;color:#fff;font-family:"Roboto",sans-serif;font-size:14px;transform:translateX(-50%)}
.nav .active{background:var(--yellow);color:var(--dark);width:113px;text-align:center;transform:none}
.hero{left:0;top:177px;width:1200px;height:474px;background:linear-gradient(120deg,#d8c9b8,#c9b79e 40%,#b8a58d 70%,#9f8f7f)}
.hero-books{left:748px;top:306px;width:363px;height:227px;background:linear-gradient(160deg,#8ac23f,#d23f6a 55%,#3a8fd0);border-radius:10px}
.hero-panel{left:141px;top:352px;width:567px;height:142px;background:rgba(255,255,255,.85)}
.hero-panel h1{position:absolute;left:22px;top:14px;font-family:"Roboto",sans-serif;font-weight:500;font-size:32px;color:var(--dark)}
.hero-panel p{position:absolute;left:22px;top:58px;font-size:15px;font-weight:700;font-family:"Roboto",sans-serif}
.btn{position:absolute;font-family:"Roboto",sans-serif;font-size:14px;text-align:center}
.btn-yellow{background:var(--yellow);color:var(--dark)}
.btn-red{background:var(--red);color:#fff}
.arrow{font-size:48px;color:#444;font-family:"Roboto",sans-serif}
.sec-grey{background:var(--grey)}
.title{position:absolute;left:0;width:1200px;text-align:center;font-family:"Roboto",sans-serif;font-weight:500;font-size:34px;color:var(--dark)}
.title b{color:var(--red);font-weight:500}
.divider{position:absolute;left:520px;width:160px;height:20px}
.about-photo{left:141px;top:726px;width:301px;height:392px;background:linear-gradient(160deg,#d9dde2,#9db3cc 50%,#3d6da8)}
.about-title{left:499px;top:716px;font-family:"Roboto",sans-serif;font-weight:500;font-size:34px;color:var(--dark)}
.about-title b{color:var(--red);font-weight:500}
.about-lead{left:499px;top:824px;width:558px;font-size:16px;line-height:24px;font-weight:600;color:var(--dark)}
.about-body{left:499px;top:910px;width:558px;font-size:12.5px;line-height:24px;color:var(--muted)}
.product{width:197px;height:197px}
.product .label{position:absolute;left:0;bottom:0;width:100%;height:38px;background:rgba(0,0,0,.55);color:#fff;text-align:center;line-height:38px;font-family:"Roboto",sans-serif;font-size:14px}
.steps-label{position:absolute;width:150px;text-align:center;font-size:14px;line-height:18px;transform:translateX(-50%);color:var(--dark)}
.testi{left:0;top:2166px;width:1200px;height:447px;background:var(--yellow)}
.avatar{left:227px;top:2332px;width:136px;height:136px;border-radius:50%;border:6px solid var(--green);background:linear-gradient(160deg,#f4e6da,#c9a58a)}
.quote{left:390px;top:2343px;width:585px;font-size:12.5px;line-height:23px;color:var(--dark)}
.why-box{width:195px;height:116px;color:#fff;font-family:"Roboto",sans-serif;font-size:14px;text-align:center;padding-top:56px;line-height:18px}
.why-icon{position:absolute;left:56px;top:-41px;width:82px;height:82px;border-radius:50%;background:#fff;box-shadow:0 2px 6px rgba(0,0,0,.25);display:flex;align-items:center;justify-content:center}
.footer{left:0;top:3021px;width:1200px;height:324px;background:var(--dark);color:#ddd}
.footer-nav span{position:absolute;top:3056px;font-family:"Roboto",sans-serif;font-size:13px;color:#eee;transform:translateX(-50%)}
.fhead{position:absolute;top:3136px;font-family:"Roboto",sans-serif;font-size:16px;color:#fff}
.finput{position:absolute;left:143px;width:218px;height:34px;background:#fff;color:#555;font-size:11px;padding:10px}
.fline{position:absolute;display:flex;gap:12px;font-size:12px;line-height:18px;color:#eee}
.bottom{left:0;top:3345px;width:1200px;height:58px;background:var(--darker);color:#ccc;font-size:12px}
</style>
</head>
<body>

<div class="abs topbar">
  <div class="abs lang">ENG ▾</div>
  <div class="abs contact" style="left:771px">
    <span class="dot-red"><svg width="14" height="14" viewBox="0 0 24 24"><path fill="#fff" d="M6.6 10.8a15 15 0 006.6 6.6l2.2-2.2c.3-.3.7-.4 1-.2 1.1.4 2.3.6 3.6.6.6 0 1 .4 1 1V20c0 .6-.4 1-1 1A17 17 0 013 4c0-.6.4-1 1-1h3.5c.6 0 1 .4 1 1 0 1.3.2 2.5.6 3.6.1.3 0 .7-.2 1z"/></svg></span>555 0142
  </div>
  <div class="abs contact" style="left:885px">
    <span class="dot-red"><svg width="14" height="14" viewBox="0 0 24 24"><path fill="#fff" d="M3 5h18v14H3zm2 2v.5l7 4.5 7-4.5V7l-7 4.5z"/></svg></span>verk@vindabrot.is
  </div>
</div>

<div class="abs header">
  <div class="abs brand" style="left:141px;top:22px;font-size:34px"><span class="brand-mark"></span>VINDABROT</div>
  <div class="abs search">SEARCH</div>
  <div class="abs search-go">GO</div>
  <svg class="abs" style="left:1030px;top:74px" width="24" height="22" viewBox="0 0 24 22"><path fill="#222" d="M2 4h20l-2 13H4z"/><circle cx="20" cy="3" r="3" fill="#fff" stroke="#222"/></svg>
</div>

<div class="abs nav">
  <span class="active" style="left:141px">HOME</span>
  <span style="left:322px">ABOUT US</span>
  <span style="left:467px">SERVICES ▾</span>
  <span style="left:658px">OUR PRODUCTS</span>
  <span style="left:812px">JOB SUBMIT</span>
  <span style="left:975px">CONTACT US</span>
</div>

<div class="abs hero" role="img" aria-label="Blurred photo of a colour swatch fan"></div>
<div class="abs hero-books" role="img" aria-label="Illustration of a stack of colourful books"></div>
<div class="abs hero-panel">
  <h1>WE ARE A PRINT FIRM IN ICELAND.</h1>
  <p>WE PROVIDE SERVICES TO STUDENTS, SCHOOLS, ETC.</p>
</div>
<div class="btn btn-yellow" style="left:163px;top:447px;width:139px;height:43px;line-height:43px">CONTACT US</div>
<div class="abs arrow" style="left:82px;top:382px">‹</div>
<div class="abs arrow" style="left:1092px;top:382px">›</div>

<div class="abs sec-grey" style="left:0;top:651px;width:1200px;height:540px"></div>
<div class="abs about-photo" role="img" aria-label="Photo of a smiling student with a backpack giving a thumbs up"></div>
<div class="abs about-title"><b>ÁBOUT</b> VINDABROT</div>
<svg class="abs" style="left:499px;top:784px" width="560" height="20"><rect x="0" y="3" width="14" height="14" fill="var(--yellow)"/><rect x="3" y="6" width="8" height="8" fill="var(--red)"/><line x1="24" y1="10" x2="560" y2="10" stroke="#999" stroke-dasharray="2 3"/></svg>
<p class="abs about-lead">Vindabrot is a company located on the university campus, which has specialized in servicing school staff, as well as providing general public printing.</p>
<p class="abs about-body">Vindabrot prints out first-class textbooks for seminars, thesis for doctors-masters- and bachelors-degrees, plus working on whole lot of smaller pieces for students, teachers and organizations. These include brochures, reports, questionnaires, business cards, books, OCR scanning and more.Vindabrot is a Heron certificated printing company. The Heron is the official ecolabel of the Nordic countries, which has created a foothold in this country and is known among consumers.</p>
<div class="btn btn-red" style="left:499px;top:1082px;width:141px;height:36px;line-height:36px">READ MORE</div>

<div class="title" style="top:1248px"><b>ÓUR</b> PRÓDUCTS</div>
<svg class="divider" style="top:1312px" viewBox="0 0 160 20"><line x1="0" y1="10" x2="68" y2="10" stroke="#999" stroke-dasharray="2 3"/><rect x="73" y="3" width="14" height="14" fill="var(--yellow)"/><rect x="76" y="6" width="8" height="8" fill="var(--red)"/><line x1="92" y1="10" x2="160" y2="10" stroke="#999" stroke-dasharray="2 3"/></svg>
<div class="abs arrow" style="left:92px;top:1428px;font-size:40px">‹</div>
<div class="abs arrow" style="left:1074px;top:1428px;font-size:40px">›</div>
<div class="abs product" style="left:166px;top:1363px;background:linear-gradient(160deg,#c98a4a,#1d3f63 60%,#c9332f)" role="img" aria-label="Photo of business cards"><div class="label">BUSINESS CARDS</div></div>
<div class="abs product" style="left:388px;top:1363px;background:linear-gradient(160deg,#e6e3de,#b9b2a8)" role="img" aria-label="Photo of printed posters"><div class="label">POSTERS</div></div>
<div class="abs product" style="left:612px;top:1363px;background:linear-gradient(90deg,#eee,#b8252a 50%,#f2f2f2)" role="img" aria-label="Photo of leaflets and brochures"><div class="label">LEAFLETS</div></div>
<div class="abs product" style="left:837px;top:1363px;background:linear-gradient(160deg,#3a3a3a,#9a9a9a 50%,#e8e8e8)" role="img" aria-label="Photo of an open printed book"><div class="label">BOOKPRINTING</div></div>
<div class="btn btn-red" style="left:508px;top:1597px;width:182px;height:38px;line-height:38px">VIEW ALL PRODUCTS</div>

<div class="abs sec-grey" style="left:0;top:1706px;width:1200px;height:460px"></div>
<div class="title" style="top:1763px"><b>HÓW</b> IT WÓRKS</div>
<svg class="divider" style="top:1829px" viewBox="0 0 160 20"><line x1="0" y1="10" x2="68" y2="10" stroke="#999" stroke-dasharray="2 3"/><rect x="73" y="3" width="14" height="14" fill="var(--yellow)"/><rect x="76" y="6" width="8" height="8" fill="var(--red)"/><line x1="92" y1="10" x2="160" y2="10" stroke="#999" stroke-dasharray="2 3"/></svg>
<svg class="abs" style="left:0;top:1860px" width="1200" height="220" viewBox="0 1860 1200 220">
  <g fill="none" stroke="#333" stroke-width="2" stroke-dasharray="5 4">
    <path d="M290 1905 Q340 1860 395 1895"/><path d="M635 1905 Q685 1860 740 1895"/>
    <path d="M470 2040 Q520 2080 565 2035"/><path d="M810 2040 Q860 2080 905 2035"/>
  </g>
  <g fill="#333"><path d="M395 1895l-10-2 6-7z"/><path d="M740 1895l-10-2 6-7z"/><path d="M565 2035l-1 10 -8-5z"/><path d="M905 2035l-1 10 -8-5z"/></g>
  <g stroke="#fff" stroke-width="8">
    <circle cx="256" cy="1969" r="62" fill="var(--green)"/>
    <circle cx="426" cy="1969" r="62" fill="var(--red)"/>
    <circle cx="599" cy="1969" r="62" fill="var(--green)"/>
    <circle cx="769" cy="1969" r="62" fill="var(--red)"/>
    <circle cx="941" cy="1969" r="62" fill="var(--green)"/>
  </g>
  <g fill="none" stroke="#fff" stroke-width="3">
    <rect x="238" y="1952" width="28" height="34"/><rect x="246" y="1958" width="20" height="22"/>
    <rect x="404" y="1950" width="44" height="32"/><path d="M426 1982v8M414 1990h24M416 1972l16-14"/>
    <rect x="581" y="1951" width="36" height="36" stroke-dasharray="5 3"/><path d="M588 1968l9 9 16-20"/>
    <rect x="747" y="1953" width="44" height="32" rx="3"/><path d="M747 1962h44M754 1977h14"/>
    <rect x="917" y="1950" width="46" height="36"/><path d="M924 1960h20M924 1968h32M924 1976h32"/><path d="M962 1945l4 4m0-4l-4 4"/>
  </g>
</svg>
<div class="steps-label" style="left:256px;top:2062px">Select Product</div>
<div class="steps-label" style="left:426px;top:2062px">Customise It By<br>Your Choice</div>
<div class="steps-label" style="left:599px;top:2062px">Finalise</div>
<div class="steps-label" style="left:769px;top:2062px">Checkout &amp; Add<br>Your Details</div>
<div class="steps-label" style="left:941px;top:2062px">Enjoy Your<br>Products</div>

<div class="abs testi"></div>
<div class="title" style="top:2228px"><b>CLIENT</b> TESTIMÓNIÁLS</div>
<svg class="divider" style="top:2294px" viewBox="0 0 160 20"><line x1="0" y1="10" x2="68" y2="10" stroke="#555" stroke-dasharray="2 3"/><rect x="73" y="3" width="14" height="14" fill="#fff"/><rect x="76" y="6" width="8" height="8" fill="var(--red)"/><line x1="92" y1="10" x2="160" y2="10" stroke="#555" stroke-dasharray="2 3"/></svg>
<svg class="abs" style="left:220px;top:2458px" width="760" height="20"><line x1="0" y1="10" x2="760" y2="10" stroke="#333" stroke-width="1.5"/></svg>
<div class="abs avatar" role="img" aria-label="Portrait photo of the client"></div>
<p class="abs quote"><b>❝</b> Lorem ipsum dolor sit amet, consectetur adipiscing elit, sed do eiusmod tempor incididunt ut labore et dolore magna aliqua. Ut enim veniam, quis nostrud exercitation ullamco laboris nisi ut aliquip ex ea commodo consequat. Duis aute irure dolor in reprehenderit in voluptate velit esse cillum dolore eu fugiat nulla pariatur. Excepteur sint occaecat cupidatat non proident, sunt in culpa qui officia . <b>❞</b></p>
<div class="abs" style="left:702px;top:2486px;font-size:13px;font-style:italic">- Marta Olsen</div>
<div class="abs" style="left:750px;top:2505px;font-size:11px;letter-spacing:1px">★★★★★</div>
<svg class="abs" style="left:580px;top:2530px" width="40" height="12"><circle cx="6" cy="6" r="3.5" fill="var(--red)"/><circle cx="18" cy="6" r="3.5" fill="#fff"/><circle cx="30" cy="6" r="3.5" fill="#fff"/></svg>

<div class="title" style="top:2670px"><b>WHY</b> CHÓOSE US</div>
<svg class="divider" style="top:2737px" viewBox="0 0 160 20"><line x1="0" y1="10" x2="68" y2="10" stroke="#999" stroke-dasharray="2 3"/><rect x="73" y="3" width="14" height="14" fill="var(--yellow)"/><rect x="76" y="6" width="8" height="8" fill="var(--red)"/><line x1="92" y1="10" x2="160" y2="10" stroke="#999" stroke-dasharray="2 3"/></svg>
<div class="abs why-box" style="left:181px;top:2828px;background:var(--red)">
  <span class="why-icon"><svg width="40" height="36" viewBox="0 0 40 36"><path fill="#333" d="M4 12l16-8 16 8v18l-16 6-16-6z"/><path fill="#fff" d="M20 14l12-6v4l-12 6z"/></svg></span>OVER 200 ORDERS<br>COMPLETED</div>
<div class="abs why-box" style="left:397px;top:2828px;background:var(--green)">
  <span class="why-icon"><svg width="40" height="40" viewBox="0 0 40 40"><circle cx="20" cy="14" r="8" fill="#333"/><path fill="#333" d="M6 38c0-9 6-14 14-14s14 5 14 14z"/></svg></span>GREAT CUSTOMERS<br>SERVICES</div>
<div class="abs why-box" style="left:610px;top:2828px;background:var(--yellow)">
  <span class="why-icon"><svg width="36" height="36" viewBox="0 0 36 36"><rect x="6" y="4" width="24" height="28" fill="#333"/><path stroke="#fff" stroke-width="2" d="M10 11h16M10 17h16M10 23h16"/></svg></span>SUPER QUALITY<br>&amp; VALUES</div>
<div class="abs why-box" style="left:826px;top:2828px;background:var(--darker)">
  <span class="why-icon"><svg width="44" height="32" viewBox="0 0 44 32"><rect x="2" y="4" width="26" height="18" fill="#333"/><path fill="#333" d="M28 10h8l6 7v5H28z"/><circle cx="10" cy="25" r="4" fill="#333"/><circle cx="34" cy="25" r="4" fill="#333"/></svg></span>HOME DELIVERY<br>OPTIONS</div>

<svg class="abs" style="left:0;top:3016px" width="1200" height="6"><rect width="1200" height="6" fill="var(--red)"/><rect x="150" width="150" height="6" fill="var(--yellow)"/><rect x="450" width="150" height="6" fill="var(--green)"/><rect x="750" width="150" height="6" fill="var(--yellow)"/><rect x="1050" width="150" height="6" fill="var(--green)"/></svg>
<div class="abs footer"></div>
<div class="footer-nav">
  <span style="left:198px">HOME</span><span style="left:330px">ABOUT US</span><span style="left:475px">SERVICES ▾</span><span style="left:645px">OUR PRODUCTS</span><span style="left:814px">JOB SUBMIT</span><span style="left:975px">CONTACT US</span>
</div>
<svg class="abs" style="left:141px;top:3102px" width="918" height="2"><line x1="0" y1="1" x2="918" y2="1" stroke="#555"/></svg>
<div class="fhead" style="left:143px">Sign Up For Newsletter</div>
<div class="finput" style="top:3175px">Name</div>
<div class="finput" style="top:3216px">Email</div>
<div class="btn btn-red" style="left:143px;top:3261px;width:61px;height:30px;line-height:30px;font-size:13px">SEND</div>
<div class="fhead" style="left:420px">Contact Details</div>
<div class="fline" style="left:420px;top:3172px"><svg width="12" height="16" viewBox="0 0 12 16"><path fill="#fff" d="M6 0a6 6 0 016 6c0 4-6 10-6 10S0 10 0 6a6 6 0 016-6zm0 4a2 2 0 100 4 2 2 0 000-4z"/></svg><span>VINDABROT<br>Kt: 410199-2270 Lindargata 9,<br>101 Reykjavík.</span></div>
<div class="fline" style="left:420px;top:3236px"><svg width="12" height="14" viewBox="0 0 24 24"><path fill="#fff" d="M6.6 10.8a15 15 0 006.6 6.6l2.2-2.2c.3-.3.7-.4 1-.2 1.1.4 2.3.6 3.6.6.6 0 1 .4 1 1V20c0 .6-.4 1-1 1A17 17 0 013 4c0-.6.4-1 1-1h3.5c.6 0 1 .4 1 1 0 1.3.2 2.5.6 3.6.1.3 0 .7-.2 1z"/></svg><span>555-0142</span></div>
<div class="fline" style="left:420px;top:3270px"><svg width="12" height="14" viewBox="0 0 24 24"><path fill="#fff" d="M3 5h18v14H3zm2 2v.5l7 4.5 7-4.5V7l-7 4.5z"/></svg><span>verk@vindabrot.is</span></div>
<div class="fhead" style="left:664px">Location Map</div>
<div class="abs" style="left:664px;top:3175px;width:180px;height:120px;background:linear-gradient(135deg,#e6ebef,#cfd9e3);border:2px solid #fff" role="img" aria-label="Map showing the shop location"></div>
<div class="fhead" style="left:912px">Connect With Us</div>
<div class="abs brand" style="left:916px;top:3208px;font-size:20px;color:#fff;gap:8px"><span class="brand-mark" style="width:22px;height:22px"></span>VINDABROT</div>
<svg class="abs" style="left:922px;top:3282px" width="110" height="22"><circle cx="11" cy="11" r="10" fill="#3b5a98"/><circle cx="35" cy="11" r="10" fill="#2aa3dd"/><circle cx="59" cy="11" r="10" fill="#d8412f"/><circle cx="83" cy="11" r="10" fill="#f39a1d"/></svg>
<div class="abs bottom">
  <span class="abs" style="left:143px;top:21px">Copyright © 2018, Vindabrot. All Right Reserved</span>
  <svg class="abs" style="left:984px;top:17px" width="74" height="24"><rect x="0" y="0" width="34" height="22" rx="2" fill="#fff"/><rect x="40" y="0" width="34" height="22" rx="2" fill="#fff"/></svg>
</div>

</body>
</html>
```